New Business Card Design Project

possibly double-sided card, with one side in color. leaves, a tree branch, or a tree of life, like laurel, olive, pine ... or a seed that grows. visual discreet and stylized or naive. no photo. no human silhouette Modern Typo possibly rounded corners matte paper, no selective varnish, neither gold nor silver English brief Double sided business card, with eventually a single colored side. Leaves, a tree branch or a tree of life, laurel, olive tree, pine tree ... or a growing seed. The design has to be discreet and stylized or naive. No human silhouettes Modern made Possibly rounded corners Matte paper, no selective varnish, no gold, no silver
Updates

I really prefer toned or subtles tones, Bluish / greenwich gray, verdigris ... Elegant and discreet colors Write "HUMANISTIC HYPNOTHERAPY, SYMBOLIC THERAPY" on 2 lines and on One side only (not with the name and address) Not use pictogram (such , address...)

Contact Information for Business Card

Hypnothérapie humaniste
Thérapie symbolique

Mireille Fontanel
Hypnothérapeute
06 48 17 35 82
84 rue des Glycines, 33990 Valcourt-sur-Jalle
therapie.fontanel@exemplemail.fr

Colors
33b8a4
3176b5

Requirements
Must have
• sober, elegant and refined card Sober design, elegant, plain
Nice to have
• desired colors: gray, blue-gis, greyish, khaki ... Desired colors: gray, blue-gray, grayish green, khaki, ...
Should not have
• gaudy colors, bright greens no bright gold neon colors

```html
<!DOCTYPE html>
<html lang="fr">
<head>
<meta charset="utf-8">
<title>Mireille Fontanel – Carte de visite</title>
<link rel="stylesheet" href="https://fonts.googleapis.com/css2?family=Noto+Serif:wght@700&family=Arimo:wght@400&display=swap">
<style>
  :root {
    --page-bg: #e4e6e6;
    --card-front: #22b9a4;
    --card-back: #ffffff;
    --ink-blue: #1f5596;
    --ink-dark: #111111;
    --ink-grey: #3f3f3f;
    --leaf-dark: #2f6b33;
    --leaf-mid: #4f8f4a;
    --leaf-light: #a9c99b;
  }
  * { margin: 0; padding: 0; box-sizing: border-box; }
  html, body {
    width: 1065px; height: 1200px; overflow: hidden;
    background: var(--page-bg);
  }
  .canvas { position: relative; width: 1065px; height: 1200px; }
  .card {
    position: absolute; left: 106px; width: 894px; height: 511px;
    border-radius: 51px;
  }
  .card--front { top: 60px; background: var(--card-front); }
  .card--back { top: 609px; background: var(--card-back); }

  .identity {
    position: absolute; left: 88px; top: 232px; width: 340px;
    text-align: center;
  }
  .identity__name {
    font-family: "Noto Serif", Georgia, serif; font-weight: 700;
    font-size: 26px; line-height: 28px; color: var(--ink-blue);
    text-transform: uppercase; letter-spacing: -0.3px;
  }
  .identity__role {
    font-family: "Arimo", Arial, sans-serif; font-size: 16px;
    line-height: 18px; color: var(--ink-dark);
  }
  .divider {
    position: absolute; left: 447px; top: 231px; width: 2px; height: 50px;
    background: var(--ink-blue);
  }
  .contact {
    position: absolute; left: 502px; top: 233px; list-style: none;
    font-family: "Arimo", Arial, sans-serif; font-size: 16px;
    letter-spacing: 1.4px; color: var(--ink-dark);
  }
  .contact__item { display: flex; align-items: center; height: 22px; }
  .contact__icon { width: 14px; height: 14px; margin-right: 13px; fill: var(--ink-blue); }
  .address {
    position: absolute; left: 0; right: 0; top: 415px; text-align: center;
    font-family: "Arimo", Arial, sans-serif; font-size: 16px;
    letter-spacing: 1.6px; color: var(--ink-dark);
  }

  .specialties {
    position: absolute; left: 0; right: 0; top: 163px; text-align: center;
    font-family: "Arimo", Arial, sans-serif; font-size: 20px;
    letter-spacing: 2.9px; line-height: 39px; color: var(--ink-grey);
  }
  .foliage {
    position: absolute; left: 303px; top: 298px; width: 281px; height: 160px;
    border-radius: 50% 50% 45% 45%;
    background: radial-gradient(ellipse at 50% 55%, var(--leaf-dark) 0%, var(--leaf-mid) 45%, var(--leaf-light) 72%, rgba(255,255,255,0) 100%);
  }
</style>
</head>
<body>
<main class="canvas">
  <section class="card card--front">
    <div class="identity">
      <h1 class="identity__name">Mireille Fontanel</h1>
      <p class="identity__role">Hypnothérapeute</p>
    </div>
    <span class="divider"></span>
    <ul class="contact">
      <li class="contact__item">
        <svg class="contact__icon" viewBox="0 0 24 24" aria-hidden="true"><path d="M6.6 10.8a15.5 15.5 0 0 0 6.6 6.6l2.2-2.2a1 1 0 0 1 1-.25 11.4 11.4 0 0 0 3.6.6 1 1 0 0 1 1 1V20a1 1 0 0 1-1 1A17 17 0 0 1 3 4a1 1 0 0 1 1-1h3.5a1 1 0 0 1 1 1c0 1.25.2 2.45.6 3.6a1 1 0 0 1-.25 1z"/></svg>
        06 48 17 35 82
      </li>
      <li class="contact__item">
        <svg class="contact__icon" viewBox="0 0 24 24" aria-hidden="true"><path d="M2 5h20v14H2z" fill-opacity=".85"/><path d="M2 5l10 8 10-8" fill="none" stroke="#22b9a4" stroke-width="1.5"/></svg>
        therapie.fontanel@exemplemail.fr
      </li>
    </ul>
    <p class="address">84 rue des Glycines, 33990 Valcourt-sur-Jalle</p>
  </section>

  <section class="card card--back">
    <p class="specialties">HYPNOTHERAPIE HUMANISTE<br>THERAPIE SYMBOLIQUE</p>
    <div class="foliage" role="img" aria-label="Branche d'olivier aux feuilles vertes"></div>
  </section>
</main>
</body>
</html>
```